Brightmere Business Card Redesign & Logo Update

We need to update our business cards to something more modern and fresh. Brightmere can provide the current color schemes and old design examples, but welcome creativity in helping us with this redesign. PLEASE NOTE that we no longer utilize the "tree" and/or "leaf" imagery in our branding. If able would apprecaite an update on the quality of our "words only" logo in Ai. / PNG formats too.

Target Market(s)

Investors, landowners, corporate partners, contractors

Industry/Entity Type

Environmental Restoration & Conservation

Contact Information for Business Card

Logo, persons name, title, mailing address, phone and email, website url

Font styles to use
Other font styles liked:
• Merriweather

Requirements
Nice to have
• Logo, persons name, title, mailing address, phone and email, website url, but open to ideams
Should not have
• No all back backgrounds

```html
<!DOCTYPE html>
<html lang="en">
<head>
<meta charset="UTF-8">
<title>Brightmere Business Card</title>
<link href="https://fonts.googleapis.com/css2?family=Merriweather:wght@400;700;900&display=swap" rel="stylesheet">
<style>
  :root {
    --backdrop: #1d1d1d;
    --paper: #ffffff;
    --brand-green: #187d40;
    --brand-orange: #ea7d22;
    --ink: #1a1a1a;
  }
  * { margin: 0; padding: 0; box-sizing: border-box; }
  html, body { width: 1200px; height: 1000px; overflow: hidden; }
  body {
    background: var(--backdrop);
    font-family: "Merriweather", Georgia, serif;
    color: var(--ink);
  }
  .card {
    position: absolute;
    left: 250px;
    width: 700px;
    height: 400px;
    background: var(--paper);
    overflow: hidden;
  }
  .card--front { top: 60px; }
  .card--back { top: 540px; }

  .wordmark {
    font-weight: 900;
    color: var(--brand-green);
    letter-spacing: 0.5px;
  }
  .card--front .wordmark {
    position: absolute;
    left: 44px;
    top: 56px;
    font-size: 44px;
  }

  .holder {
    position: absolute;
    right: 44px;
    top: 72px;
    text-align: right;
  }
  .holder__name { font-size: 24px; font-weight: 700; letter-spacing: 0.5px; }
  .holder__first { color: var(--brand-orange); }
  .holder__last { color: var(--brand-green); }
  .holder__title { font-size: 17px; margin-top: 4px; }

  .divider {
    position: absolute;
    left: 120px;
    top: 168px;
    width: 410px;
    height: 2px;
    background: var(--brand-orange);
  }

  .address {
    position: absolute;
    right: 44px;
    top: 196px;
    text-align: right;
    font-size: 15px;
    line-height: 1.55;
  }

  .contacts {
    position: absolute;
    left: 86px;
    top: 194px;
    list-style: none;
    font-size: 16px;
    line-height: 1.55;
  }
  .contacts li { display: flex; align-items: center; gap: 10px; }
  .contacts svg { width: 14px; height: 14px; flex: none; }

  .bands { position: absolute; left: 0; bottom: 0; width: 700px; height: 130px; }

  .card--back {
    display: flex;
    align-items: center;
    justify-content: center;
    gap: 18px;
  }
  .brand-dot {
    width: 70px;
    height: 70px;
    border-radius: 50%;
    background: var(--brand-green);
  }
  .card--back .wordmark { font-size: 58px; }
</style>
</head>
<body>

<section class="card card--front">
  <div class="wordmark">Brightmere</div>

  <div class="holder">
    <div class="holder__name"><span class="holder__first">NOLAN</span> <span class="holder__last">REYES</span></div>
    <div class="holder__title">Founder</div>
  </div>

  <div class="divider"></div>

  <ul class="contacts">
    <li>
      <svg viewBox="0 0 14 14" aria-hidden="true"><path d="M3 1 L5.5 1 L6.5 4 L5 5.2 Q6.3 8 8.8 9 L10 7.5 L13 8.5 L13 11 Q12.5 13 10.5 13 Q1 12 1 3.5 Q1 1.5 3 1 Z" fill="var(--brand-orange)"/></svg>
      (555) 014-2290
    </li>
    <li>
      <svg viewBox="0 0 14 14" aria-hidden="true"><rect x="1" y="3" width="12" height="8" fill="var(--brand-orange)"/><path d="M1 3 L7 8 L13 3" fill="none" stroke="#fff" stroke-width="1.2"/></svg>
      hello@brightmeremail.com
    </li>
    <li>
      <svg viewBox="0 0 14 14" aria-hidden="true"><circle cx="7" cy="7" r="6" fill="var(--brand-orange)"/><path d="M1 7 H13 M7 1 Q3.5 7 7 13 M7 1 Q10.5 7 7 13" fill="none" stroke="#fff" stroke-width="0.9"/></svg>
      www.brightmere-eco.com
    </li>
  </ul>

  <div class="address">
    Your Company Address<br>
    Rd No. 48, PO 2710, NV
  </div>

  <svg class="bands" viewBox="0 0 700 130" aria-hidden="true">
    <polygon points="0,58 466,58 464,66 0,66" fill="var(--brand-green)"/>
    <polygon points="0,74 462,74 454,130 0,130" fill="var(--brand-orange)"/>
    <polygon points="472,34 700,34 700,130 458,130" fill="var(--brand-green)"/>
  </svg>
</section>

<section class="card card--back">
  <div class="brand-dot"></div>
  <div class="wordmark">Brightmere</div>
</section>

</body>
</html>
```